Psychotherapy, Life Coaching, Writer, Motivational Speaker

I am a psychotherapist, life coach, writer and speaker on health and wellness issues. I am a humanist - who believes that we are born to self-actualize - but life - changes that course. That we develop armor and coping mechanisms that divert our growth. I help people examine their road blocks to happiness. My business is unique in that I do concierge therapy. I work intensively - with multi-day sessions, I work internationally through tele-therapy - and traditionally - in an office space. My work is tailored to your needs.

Target Market(s)

Broad

Industry/Entity Type

Health

Contact Information for Business Card

Listen And Mend
Tim Harwell
482 East 29th Avenue
New York, NY 10027
(305) 555-0187

Requirements
Must have
• Clean lines... not too busy...
• FB page listing: Listen And Mend
• my Web page: www.listenandmend.example
Nice to have
• I would love to be able to list the services: Psychotherapist, Life Coach, Motivational Speaker and Writer - but also don't want a crazy crowded card. Feel free to use the back for description.
Should not have
• Stay away from corny imagery - lotus flowers, zen, lily pond, clouds.

```html
<!DOCTYPE html>
<html lang="en">
<head>
<meta charset="utf-8">
<title>Listen And Mend – Business Card</title>
<link href="https://fonts.googleapis.com/css2?family=Lato:wght@400;700&display=swap" rel="stylesheet">
<style>
  :root {
    --backdrop: #e6e6e6;
    --card: #ffffff;
    --brand-blue: #4f7fb9;
    --ink: #1a1a1a;
    --panel-black: #000000;
    --reverse-text: #f2f2f2;
  }
  * { margin: 0; padding: 0; box-sizing: border-box; }
  html, body {
    width: 1200px; height: 720px; overflow: hidden;
    background: var(--backdrop);
    font-family: "Lato", Arial, sans-serif;
    color: var(--ink);
  }
  .stage { position: relative; width: 1200px; height: 720px; }
  .card {
    position: absolute; top: 241px; width: 419px; height: 239px;
    background: var(--card); border-radius: 14px; overflow: hidden;
  }
  .card--front { left: 148px; }
  .card--back { left: 633px; }

  .front-panel { position: absolute; inset: 0; }

  .brand-name {
    position: absolute; font-weight: 700; color: var(--brand-blue); white-space: nowrap;
  }
  .card--front .brand-name { left: 13px; top: 37px; font-size: 20px; }
  .card--back .brand-name { left: 15px; top: 23px; font-size: 23px; }

  .contact-list { position: absolute; left: 10px; top: 86px; list-style: none; font-size: 13.5px; line-height: 16px; }
  .contact-list li { display: flex; align-items: center; gap: 3px; white-space: nowrap; }
  .contact-icon { width: 11px; height: 11px; flex: none; }

  .address { position: absolute; left: 12px; top: 181px; font-size: 12px; line-height: 14.5px; }

  .person { position: absolute; right: 13px; top: 106px; text-align: right; white-space: nowrap; }
  .person-name { font-size: 15px; color: var(--reverse-text); }
  .person-name strong { color: var(--brand-blue); font-weight: 700; }
  .person-role { font-size: 13px; color: var(--reverse-text); margin-top: 2px; }

  .appointment { position: absolute; left: 17px; top: 111px; font-size: 13.5px; white-space: nowrap; }
  .services { position: absolute; right: 11px; top: 170px; text-align: right; font-size: 14.5px; line-height: 18px; }
</style>
</head>
<body>
<main class="stage">
  <section class="card card--front" aria-label="Card front">
    <svg class="front-panel" viewBox="0 0 419 239" preserveAspectRatio="none" aria-hidden="true">
      <path d="M250,0 Q172,130 252,239 L419,239 L419,0 Z" fill="var(--brand-blue)"/>
      <path d="M282,0 Q196,130 252,239 L419,239 L419,0 Z" fill="var(--panel-black)"/>
    </svg>
    <h1 class="brand-name">Listen And Mend</h1>
    <ul class="contact-list">
      <li>
        <svg class="contact-icon" viewBox="0 0 12 12" aria-hidden="true"><path d="M1 4 Q6 0 11 4 L10 6 L8 5 L8 4 Q6 3 4 4 L4 5 L2 6 Z M3 7 H9 L10 11 H2 Z" fill="var(--brand-blue)"/></svg>
        (305) 555-0187
      </li>
      <li>
        <svg class="contact-icon" viewBox="0 0 12 12" aria-hidden="true"><rect x="0.5" y="2" width="11" height="8" rx="1" fill="var(--brand-blue)"/><path d="M1 3 L6 7 L11 3" stroke="#fff" fill="none" stroke-width="1"/></svg>
        tharwellcare@mail.example
      </li>
      <li>
        <svg class="contact-icon" viewBox="0 0 12 12" aria-hidden="true"><circle cx="6" cy="6" r="5.3" fill="var(--brand-blue)"/><path d="M1 6 H11 M6 0.7 V11.3 M6 0.7 Q2.5 6 6 11.3 M6 0.7 Q9.5 6 6 11.3" stroke="#fff" stroke-width="0.8" fill="none"/></svg>
        www.listenandmend.example
      </li>
      <li>
        <svg class="contact-icon" viewBox="0 0 12 12" aria-hidden="true"><rect x="0.5" y="0.5" width="11" height="11" rx="1.5" fill="var(--brand-blue)"/></svg>
        Listen And Mend
      </li>
    </ul>
    <address class="address" style="font-style:normal">482 East 29th Avenue<br>New York, NY 10027</address>
    <div class="person">
      <p class="person-name"><strong>Tim Harwell</strong>, LMHC, NCC</p>
      <p class="person-role">Psychotherapist.</p>
    </div>
  </section>

  <section class="card card--back" aria-label="Card back">
    <h2 class="brand-name">Listen and Mend</h2>
    <p class="appointment">Your Next Appoinment is at...................... at.............. am/pm</p>
    <p class="services">Psychotherapy,<br>Coaching,<br>Wellness Media</p>
  </section>
</main>
</body>
</html>
```